Law Firm Letterhead

We are looking for a letterhead for our military/veterans law firm. We like simplicity and clean, modern, flat, uncluttered designs. Our logo font is DIN 1451, and our website/business card info font is Helvetica Neue.

Required Information:

- Logo/Graphic: Please see attached logo / business card for ideas. Please also review firm website.

- Motto: A law firm for service members and veterans

- Web Address: www.brightharborcounsel.example

- Email: info@brightharborcounsel.example

- Phone: 866-214-3097

Colors: We prefer either a blue/grey or an all-blue color scheme. The blue in our logo is #336699.

Please DO NOT submit more than 3 designs. Spamming designs with only minor changes between the designs is not appreciated. We can evaluate your quality and direction by your best 1 or 2 designs.

Thank you!

```html
<!DOCTYPE html>
<html lang="en">
<head>
<meta charset="utf-8">
<title>Bright Harbor Counsel — Letterhead</title>
<link rel="stylesheet" href="https://fonts.googleapis.com/css2?family=Barlow+Condensed:wght@600&family=Arimo:wght@400&display=swap">
<style>
  :root {
    --brand-blue: #336699;
    --band-blue: #6687b3;
    --paper: #ffffff;
    --on-blue: #ffffff;
  }
  * { margin: 0; padding: 0; box-sizing: border-box; }
  html, body { width: 849px; height: 1200px; overflow: hidden; background: var(--paper); }
  .letterhead {
    position: relative;
    width: 849px;
    height: 1200px;
    background: var(--paper);
    font-family: "Arimo", "Helvetica Neue", Helvetica, Arial, sans-serif;
  }
  .firm-name {
    position: absolute;
    top: 16px;
    left: 0;
    width: 100%;
    text-align: center;
    font-family: "Barlow Condensed", "DIN 1451", sans-serif;
    font-weight: 600;
    color: var(--brand-blue);
    text-transform: uppercase;
    line-height: 1;
  }
  .firm-name .line-primary {
    display: block;
    font-size: 58px;
    letter-spacing: 1px;
  }
  .firm-name .line-secondary {
    display: block;
    margin-top: 6px;
    font-size: 34px;
    letter-spacing: 9px;
    padding-left: 9px;
  }
  .motto-band {
    position: absolute;
    top: 140px;
    left: 0;
    width: 100%;
    height: 26px;
    background: var(--band-blue);
    color: var(--on-blue);
    font-size: 20px;
    letter-spacing: 1.2px;
    line-height: 26px;
    text-align: center;
  }
  .contact-footer {
    position: absolute;
    left: 0;
    bottom: 0;
    width: 100%;
    height: 87px;
    background: var(--brand-blue);
    color: var(--on-blue);
    font-size: 15.5px;
  }
  .contact-item {
    position: absolute;
    top: 34px;
    white-space: nowrap;
    letter-spacing: -0.2px;
  }
  .contact-web { left: 21px; }
  .contact-email { left: 338px; }
  .contact-phone { left: 662px; }
</style>
</head>
<body>
  <div class="letterhead">
    <header>
      <h1 class="firm-name">
        <span class="line-primary">Bright Harbor</span>
        <span class="line-secondary">Counsel</span>
      </h1>
      <p class="motto-band">A law firm for service members and veterans</p>
    </header>

    <footer class="contact-footer">
      <span class="contact-item contact-web">W : www.brightharborcounsel.example</span>
      <span class="contact-item contact-email">E : info@brightharborcounsel.example</span>
      <span class="contact-item contact-phone">P : 866-214-3097</span>
    </footer>
  </div>
</body>
</html>
```